Homeopathic medicinal cream label design

I am looking for a product label design for a medicinal (cannabis) topical cream to be sold to medical marijuana patients. It is a new product that has not yet established a brand identity. It will be sold in 2 and 4 ounce containers so the design needs to work on a small scale. The design may be used for other branding as well.

Target Market(s)

Medical marijuana users in states where it is legal. The product should appeal to both men and women to promote pain relief in muscles and joints. It can also be used as a massage cream for general relaxation.

Industry/Entity Type

Medical

Font styles to use
Sans Serif

Requirements
Must have
• Something that reflects the company name - The Quiet Heron - and the name of the initial product - Meadow Balm Blend.
• In addition to the name of the company and the name of the product, other information to include would be the volume being sold (e.g. 4 oz.), that it is a topical botanical ointment, and its ingredients (coconut oil, beeswax, soy lecithin, and eight all natural botanical oils - cannabis, lavender, eucalyptus, peppermint, rosemary, cinnamon, clove, and lemon). The label should clearly state that the product is for topical use only.
• The information must fit on the space available on the package. The 4 oz. container's lid has approximately 2 1/8" of surface area. The width of the label on the lid should be approximately 1 7/8". On the container's body, the height of the surface area is approximately 1", and the width is approximately 8 1/2 inches. The width of the label should be around 8 inches to allow room for it to be applied to the container. I have posted a photo of the 4 oz. container and the 2 oz. container. I have also posted a photo of the labeling of some of our competitors with similar products.
Nice to have
• We are thinking of having the logo on the lid of the container, and a circle bordering the lid that may have text in it. (See the "Amber Moth" label attached as an exemplar).
• The label on the body of the container (or maybe on the bottom on the container) would list other information about the product, such as its ingredients and our contact information.

```html
<!DOCTYPE html>
<html lang="en">
<head>
<meta charset="utf-8">
<title>The Quiet Heron – Meadow Balm Blend lid labels</title>
<link rel="stylesheet" href="https://fonts.googleapis.com/css2?family=Open+Sans:wght@400;600;700;800&display=swap">
<style>
  :root {
    --leaf-green: #7cc242;
    --ink-grey: #4a4a4a;
    --rule-grey: #9a9a9a;
    --label-white: #ffffff;
    --stage: #f1efe9;
    --pattern-dark: #5a5a5a;
    --pattern-light: #c9c9c9;
  }
  html, body {
    margin: 0;
    padding: 0;
    width: 1200px;
    height: 900px;
    overflow: hidden;
    background: var(--stage);
    font-family: "Open Sans", Arial, sans-serif;
  }
  .canvas {
    position: relative;
    width: 1200px;
    height: 900px;
  }
  .lid-label {
    position: absolute;
    display: block;
  }
  .lid-label--large { left: 80px; top: 140px; width: 540px; height: 540px; }
  .lid-label--small { left: 750px; top: 235px; width: 380px; height: 380px; }

  .ring-band { fill: var(--leaf-green); }
  .ring-text { fill: var(--label-white); font-size: 13px; font-weight: 400; letter-spacing: 0.3px; }
  .center-disc { fill: var(--label-white); }
  .brand-name { fill: var(--ink-grey); font-size: 22px; font-weight: 600; }
  .brand-dot { fill: var(--leaf-green); }
  .product-name { fill: var(--leaf-green); font-size: 44px; font-weight: 800; letter-spacing: -0.5px; }
  .product-sub { fill: var(--ink-grey); font-size: 40px; font-weight: 700; letter-spacing: -0.5px; }
  .rule { stroke: var(--rule-grey); stroke-width: 1; }
  .tagline { fill: var(--leaf-green); font-size: 17px; font-weight: 400; }
  .net-weight { fill: var(--ink-grey); font-size: 17px; font-weight: 700; }
</style>
</head>
<body>
<main class="canvas">

  <svg class="lid-label lid-label--large" viewBox="0 0 500 500" aria-label="Meadow Balm Blend 4 oz lid label">
    <defs>
      <radialGradient id="pattern-tone-large" cx="50%" cy="50%" r="50%">
        <stop offset="66%" stop-color="var(--pattern-light)"/>
        <stop offset="80%" stop-color="var(--pattern-dark)"/>
        <stop offset="92%" stop-color="var(--pattern-light)"/>
      </radialGradient>
      <path id="ring-top-large" d="M 18,250 A 232,232 0 1,1 482,250"/>
      <path id="ring-bottom-large" d="M 6,250 A 244,244 0 0,0 494,250"/>
    </defs>
    <circle class="ring-band" cx="250" cy="250" r="250"/>
    <path role="img" aria-label="Black and white botanical illustration of herbs, citrus, leaves and a butterfly"
          fill="url(#pattern-tone-large)" fill-rule="evenodd"
          d="M 250,22 A 228,228 0 1,1 249.9,22 Z M 250,85 A 165,165 0 1,0 250.1,85 Z"/>
    <circle class="center-disc" cx="250" cy="250" r="165"/>
    <text class="ring-text"><textPath href="#ring-top-large" startOffset="50%" text-anchor="middle">cannabis, lavender, eucalyptus, peppermint, rosemary, cinnamon, clove, and lemon</textPath></text>
    <text class="ring-text"><textPath href="#ring-bottom-large" startOffset="50%" text-anchor="middle">lorem ipsum informations · lorem ipsum informations · lorem ipsum</textPath></text>
    <circle class="brand-dot" cx="160" cy="143" r="6"/>
    <text class="brand-name" x="258" y="150" text-anchor="middle">the quiet heron</text>
    <text class="product-name" x="250" y="214" text-anchor="middle">Meadow Balm</text>
    <text class="product-sub" x="250" y="262" text-anchor="middle">Blend</text>
    <line class="rule" x1="160" y1="287" x2="340" y2="287"/>
    <text class="tagline" x="250" y="312" text-anchor="middle">8 all natural botanical oils</text>
    <line class="rule" x1="160" y1="327" x2="340" y2="327"/>
    <text class="net-weight" x="250" y="358" text-anchor="middle">4 oz</text>
  </svg>

  <svg class="lid-label lid-label--small" viewBox="0 0 500 500" aria-label="Meadow Balm Blend 2 oz lid label">
    <defs>
      <radialGradient id="pattern-tone-small" cx="50%" cy="50%" r="50%">
        <stop offset="66%" stop-color="var(--pattern-light)"/>
        <stop offset="80%" stop-color="var(--pattern-dark)"/>
        <stop offset="92%" stop-color="var(--pattern-light)"/>
      </radialGradient>
      <path id="ring-top-small" d="M 18,250 A 232,232 0 1,1 482,250"/>
      <path id="ring-bottom-small" d="M 6,250 A 244,244 0 0,0 494,250"/>
    </defs>
    <circle class="ring-band" cx="250" cy="250" r="250"/>
    <path role="img" aria-label="Black and white botanical illustration of herbs, citrus, leaves and a butterfly"
          fill="url(#pattern-tone-small)" fill-rule="evenodd"
          d="M 250,22 A 228,228 0 1,1 249.9,22 Z M 250,85 A 165,165 0 1,0 250.1,85 Z"/>
    <circle class="center-disc" cx="250" cy="250" r="165"/>
    <text class="ring-text"><textPath href="#ring-top-small" startOffset="50%" text-anchor="middle">cannabis, lavender, eucalyptus, peppermint, rosemary, cinnamon, clove, and lemon</textPath></text>
    <text class="ring-text"><textPath href="#ring-bottom-small" startOffset="50%" text-anchor="middle">lorem ipsum informations · lorem ipsum informations · lorem ipsum</textPath></text>
    <circle class="brand-dot" cx="160" cy="143" r="6"/>
    <text class="brand-name" x="258" y="150" text-anchor="middle">the quiet heron</text>
    <text class="product-name" x="250" y="214" text-anchor="middle">Meadow Balm</text>
    <text class="product-sub" x="250" y="262" text-anchor="middle">Blend</text>
    <line class="rule" x1="160" y1="287" x2="340" y2="287"/>
    <text class="tagline" x="250" y="312" text-anchor="middle">8 all natural botanical oils</text>
    <line class="rule" x1="160" y1="327" x2="340" y2="327"/>
    <text class="net-weight" x="250" y="358" text-anchor="middle">2 oz</text>
  </svg>

</main>
</body>
</html>
```